Business cards for Veterinarian
Dale Forsk, DVM
Project: Business cards for Veterinarian
Business cards for Veterinarian -
Creative Brief
Use specific fonts
Whatever works, but not curly twisty stuff that is hard to read!
Bright & Fun-filled
872 Hollin Parkway Brunswick, GA 31587
info@daleforskvet.example
daleforskvet.example
I'm thinking the front would be mostly logo and phone number and put the rest of the info on the back, just so you can see the logo/phone number better, basically..... Would also like "Located across from the QMRL" on there somewhere, as well as "Office Hours By Appointment" Could put the veterinary caduceus on there and, if room allowed, some sort of a line or something to write the time of the next appointment (may not be enough room for that - if not, no big deal.) I kinda like watermarks too, if you wanted to try something with them.

```html
<!DOCTYPE html>
<html lang="en">
<head>
<meta charset="utf-8">
<title>Dale Forsk, DVM – Business Card</title>
<link rel="stylesheet" href="https://fonts.googleapis.com/css2?family=Cabin:wght@400;600;700&display=swap">
<style>
  :root {
    --backdrop: #e9e6e1;
    --card: #ffffff;
    --ink: #4d4d4d;
    --ink-strong: #3a3a3a;
    --brown-dark: #4a3b2a;
    --taupe: #8c7c63;
    --taupe-light: #c9bfae;
    --divider: #cfcac2;
  }
  * { box-sizing: border-box; margin: 0; padding: 0; }
  html, body { width: 1200px; height: 780px; overflow: hidden; }
  body {
    background: var(--backdrop);
    font-family: "Cabin", "Gill Sans", sans-serif;
    color: var(--ink);
  }
  .canvas { position: relative; width: 1200px; height: 780px; }
  .card {
    position: absolute; left: 80px; top: 90px;
    width: 1040px; height: 600px;
    background: var(--card);
    border-radius: 34px;
    overflow: hidden;
    box-shadow: 0 10px 30px rgba(0,0,0,0.18);
  }
  .brand {
    position: absolute; left: 40px; top: 96px; width: 400px;
    text-align: center;
  }
  .brand-art {
    width: 340px; height: 200px; margin: 0 auto;
    border-radius: 14px;
    background: linear-gradient(160deg, #b7a98f 0%, #7d6c54 55%, #4a3b2a 100%);
  }
  .brand-name {
    margin-top: 12px;
    font-size: 38px; font-weight: 700;
    color: var(--brown-dark);
    letter-spacing: 0.5px;
  }
  .brand-tagline {
    margin-top: 6px;
    font-size: 16px; font-weight: 600;
    color: var(--brown-dark);
  }
  .divider {
    position: absolute; left: 472px; top: 70px;
    width: 2px; height: 310px; background: var(--divider);
  }
  .details { position: absolute; left: 505px; top: 66px; }
  .details-name {
    font-size: 34px; font-weight: 700; color: var(--ink-strong);
  }
  .details-address {
    margin-top: 26px; font-size: 23px; line-height: 1.3;
  }
  .contact-list { margin-top: 26px; list-style: none; }
  .contact-item {
    display: flex; align-items: center; gap: 14px;
    font-size: 22px; height: 40px;
  }
  .contact-icon { width: 22px; height: 22px; flex: none; }
  .details-note {
    margin-top: 12px;
    font-size: 17px; font-weight: 600;
    color: var(--taupe);
  }
  .swoosh { position: absolute; left: 0; bottom: 0; width: 1040px; height: 190px; }
</style>
</head>
<body>
<main class="canvas">
  <section class="card">
    <svg class="swoosh" viewBox="0 0 1040 190" preserveAspectRatio="none" aria-hidden="true">
      <path d="M0 120 C 250 75, 600 45, 1040 0 L1040 190 L0 190 Z" fill="var(--taupe-light)"/>
      <path d="M0 140 C 300 90, 650 60, 1040 26 L1040 190 L0 190 Z" fill="var(--brown-dark)"/>
      <path d="M0 158 C 320 112, 680 86, 1040 58 L1040 190 L0 190 Z" fill="#ffffff"/>
      <path d="M0 190 L0 176 C 300 146, 700 104, 1040 88 L1040 190 Z" fill="var(--taupe)"/>
    </svg>

    <div class="brand">
      <div class="brand-art" role="img" aria-label="Illustration of a dog and two cats behind the practice sign"></div>
      <p class="brand-name">Dale Forsk, DVM</p>
      <p class="brand-tagline">Caring for dogs and cats and their whole family!</p>
    </div>

    <div class="divider"></div>

    <div class="details">
      <h1 class="details-name">Dale Forsk, DVM</h1>
      <p class="details-address">872 Hollin Parkway<br>Brunswick, GA 31587</p>
      <ul class="contact-list">
        <li class="contact-item">
          <svg class="contact-icon" viewBox="0 0 24 24" aria-hidden="true"><path d="M6.6 10.8a15 15 0 0 0 6.6 6.6l2.2-2.2a1 1 0 0 1 1-.25 11.4 11.4 0 0 0 3.6.6 1 1 0 0 1 1 1V20a1 1 0 0 1-1 1A17 17 0 0 1 3 4a1 1 0 0 1 1-1h3.5a1 1 0 0 1 1 1c0 1.25.2 2.45.6 3.6a1 1 0 0 1-.25 1z" fill="var(--ink)"/></svg>
          <span>912-555-0148</span>
        </li>
        <li class="contact-item">
          <svg class="contact-icon" viewBox="0 0 24 24" aria-hidden="true"><circle cx="12" cy="12" r="10" fill="none" stroke="var(--ink)" stroke-width="2.4"/><circle cx="12" cy="12" r="4" fill="none" stroke="var(--ink)" stroke-width="2.4"/></svg>
          <span>info@daleforskvet.example</span>
        </li>
        <li class="contact-item">
          <svg class="contact-icon" viewBox="0 0 24 24" aria-hidden="true"><circle cx="12" cy="12" r="10" fill="none" stroke="var(--ink)" stroke-width="1.8"/><ellipse cx="12" cy="12" rx="4.5" ry="10" fill="none" stroke="var(--ink)" stroke-width="1.5"/><path d="M2 12h20M4 7h16M4 17h16" stroke="var(--ink)" stroke-width="1.5"/></svg>
          <span>www.daleforskvet.example</span>
        </li>
      </ul>
      <p class="details-note">Located across from the QMRL · Office Hours By Appointment</p>
    </div>
  </section>
</main>
</body>
</html>
```